UNIQUE, Elegant business card for transport company.

MUST BE AN ACTUAL GRAPHIC DESIGNER.
NO TEMPLATES, NO MOCKUP GENERATORS.
Looking for a top notch, head turning, business card.
Will be printed on premium luxury paper with spot glossing and debossing.
Must know how to set up for spot glossing. Must be willing to work on the file to meet printers spec after final design.

Target Market(s)

All info on .psd file

Contact Information for Business Card

All info on .psd file

Requirements
Must have
• All info on .psd file
Nice to have
• All info on .psd file
Should not have
• Nothing red

```html
<!DOCTYPE html>
<html lang="en">
<head>
<meta charset="utf-8">
<title>Velora Haul, Inc. — Business Card</title>
<link rel="stylesheet" href="https://fonts.googleapis.com/css2?family=Source+Sans+3:wght@400;600;700&display=swap">
<style>
  :root {
    --page-bg: #2a2b2e;
    --brand-blue: #156895;
    --accent-blue: #2f8fd0;
    --light-blue: #4aa6e6;
    --card-white: #ebedef;
    --card-black: #0b0b0c;
    --ink: #141414;
    --font-main: "Source Sans 3", "Myriad Pro", Arial, sans-serif;
  }
  * { box-sizing: border-box; margin: 0; padding: 0; }
  html, body { width: 1200px; height: 900px; overflow: hidden; }
  body {
    background: var(--page-bg);
    font-family: var(--font-main);
    display: flex;
    flex-direction: column;
    align-items: center;
    justify-content: center;
    gap: 48px;
  }
  .card {
    width: 640px;
    height: 366px;
    position: relative;
    overflow: hidden;
    box-shadow: 0 18px 40px rgba(0,0,0,.45);
  }

  /* Front */
  .card-front { display: flex; background: var(--card-white); }
  .front-brand {
    width: 45%;
    background: var(--brand-blue);
    display: flex;
    align-items: center;
    justify-content: center;
    gap: 12px;
  }
  .brand-dot {
    width: 22px; height: 22px; border-radius: 50%;
    background: var(--light-blue);
  }
  .front-brand .brand-name {
    color: #ffffff;
    font-weight: 700;
    font-size: 26px;
    letter-spacing: .02em;
  }
  .front-contact {
    flex: 1;
    padding: 78px 0 0 52px;
    color: var(--ink);
  }
  .person-name { font-size: 30px; font-weight: 600; line-height: 1; }
  .person-title { font-size: 15px; margin-top: 4px; }
  .phones { margin-top: 26px; font-size: 15px; line-height: 1.3; }
  .phones .label { color: var(--accent-blue); }
  .web-block {
    margin-top: 22px;
    border-left: 2px solid var(--brand-blue);
    padding-left: 10px;
    font-size: 15px;
    line-height: 1.3;
  }
  .web-block .site { color: var(--brand-blue); }

  /* Back */
  .card-back {
    background: var(--card-black);
    display: flex;
    align-items: center;
    justify-content: center;
  }
  .back-strip {
    position: absolute; top: 0; right: 0; bottom: 0;
    width: 7%;
    background: var(--brand-blue);
  }
  .back-brand {
    display: flex; align-items: center; gap: 16px;
    margin-right: 7%;
  }
  .back-brand .brand-name {
    color: var(--light-blue);
    font-weight: 700;
    font-size: 42px;
    letter-spacing: .03em;
    text-transform: uppercase;
  }
</style>
</head>
<body>
  <section class="card card-front">
    <div class="front-brand">
      <span class="brand-dot"></span>
      <span class="brand-name">Velora Haul</span>
    </div>
    <div class="front-contact">
      <p class="person-name">Dana Marsh</p>
      <p class="person-title">Transporter</p>
      <div class="phones">
        <p><span class="label">office</span> (555) 201.4830</p>
        <p><span class="label">mobile</span> (555) 377.9012</p>
      </div>
      <div class="web-block">
        <p>dana@velorahaul.com</p>
        <p class="site">www.velorahaul.com</p>
      </div>
    </div>
  </section>

  <section class="card card-back">
    <div class="back-brand">
      <span class="brand-name">Velora Haul, Inc.</span>
    </div>
    <div class="back-strip"></div>
  </section>
</body>
</html>
```